Bright And Steady Web Design & Marketing

Will award a 2nd place prize of $100.00 if someone can come up with a logo to match this design!
Updates

Okay, I'm really looking to see some better designs here. What do you think will bring the best designs out? Please remember with all future submissions I'm looking for a cartoon style / illustrator style website. I'm not sure what the technical term is for it, so I uploaded some images in the brief.

Target Market(s)

Small Business Owners

Industry/Entity Type

Marketing

Logo Text

BrightAndSteady.example

Number of Pages Required

1 page

Colors

Designer to choose colors to be used in the design.

Requirements
Must have
• Logo should say BrightAndSteady.example I would like more than just a text logo. I want some sort of cool custom graphic / icon with it that will look nice on shirts/hats/etc

```html
<!DOCTYPE html>
<html lang="en">
<head>
<meta charset="utf-8">
<title>Bright And Steady Web Design &amp; Marketing</title>
<link href="https://fonts.googleapis.com/css2?family=Exo+2:ital,wght@0,500;0,600;0,700;0,800;1,600;1,700&family=Open+Sans:ital,wght@0,400;0,600;0,700;1,400&display=swap" rel="stylesheet">
<style>
:root{
  --teal:#18c6cf;
  --green:#2fe08a;
  --grad:linear-gradient(90deg,#19c3d6 0%,#2fe08a 100%);
  --ink:#2f3336;
  --text:#555b60;
  --muted:#8a9096;
  --band:#ececec;
  --band-2:#e6e7e8;
  --dark:#3c4145;
  --white:#ffffff;
  --head:"Exo 2",sans-serif;
  --body:"Open Sans",sans-serif;
}
*{box-sizing:border-box;margin:0;padding:0}
html,body{width:1200px;height:4276px;overflow:hidden}
body{font-family:var(--body);color:var(--text);background:var(--white);position:relative}
section,header,footer{position:absolute;left:0;width:1200px;overflow:hidden}
.abs{position:absolute}
.btn{position:absolute;display:flex;align-items:center;justify-content:center;background:var(--grad);color:var(--white);font-family:var(--head);font-weight:700;font-size:20px;letter-spacing:.5px;border-radius:4px;box-shadow:0 4px 10px rgba(0,0,0,.15)}
.eyebrow{font-family:var(--head);font-weight:700;font-size:15px;color:var(--ink);letter-spacing:.5px}
.title{font-family:var(--head);font-weight:700;color:var(--ink);letter-spacing:1px;line-height:1}
.sub{font-family:var(--head);font-weight:600;font-size:17px;color:var(--teal);letter-spacing:1px}
.copy{font-style:italic;font-size:14.5px;line-height:1.75;color:var(--text)}

/* header + hero */
.hero{top:0;height:678px;background:linear-gradient(115deg,#6d5a48 0%,#3e3b3a 40%,#8a8f96 70%,#3b4046 100%)}
.hero-photo{position:absolute;inset:0;background:linear-gradient(90deg,rgba(20,22,24,.55) 0%,rgba(20,22,24,.15) 55%,rgba(20,22,24,.35) 100%)}
.nav{position:absolute;top:0;left:0;width:1200px;height:108px;background:linear-gradient(180deg,rgba(0,0,0,.6),rgba(0,0,0,0))}
.brand{position:absolute;left:80px;top:34px;font-family:var(--head);font-weight:800;font-size:27px;color:var(--white);letter-spacing:1px}
.menu{position:absolute;left:355px;top:42px;display:flex;gap:20px;font-family:var(--head);font-weight:600;font-size:14px;color:var(--white);letter-spacing:.2px;white-space:nowrap}
.menu .active{color:var(--green);display:flex;align-items:center;gap:6px}
.phone{position:absolute;left:975px;top:32px;width:145px;height:40px;border-radius:3px;background:var(--grad);color:var(--white);font-family:var(--head);font-weight:700;font-size:17px;display:flex;align-items:center;justify-content:center}
.hero h1{position:absolute;left:78px;top:308px;font-family:var(--head);font-weight:700;font-size:39px;line-height:1.17;color:var(--white);text-shadow:0 2px 6px rgba(0,0,0,.5)}
.hero .btn{left:78px;top:480px;width:250px;height:58px}
.hero-wedge{position:absolute;left:0;bottom:0}
.dots{position:absolute;left:970px;top:628px;display:flex;gap:10px}
.dots i{width:17px;height:17px;border:2px solid var(--white);border-radius:50%}
.dots i.on{background:var(--white)}

/* welcome */
.welcome{top:678px;height:505px;background:var(--white)}
.welcome .eyebrow{left:80px;top:118px}
.welcome .title{left:80px;top:146px;font-size:38px;position:absolute}
.welcome .sub{left:80px;top:192px;position:absolute}
.welcome .copy{left:80px;top:226px;width:520px;position:absolute;font-size:14px}
.welcome .btn{left:80px;top:348px;width:198px;height:52px}
.welcome-device{left:665px;top:118px;width:420px;height:260px;border-radius:10px;background:linear-gradient(135deg,#3f4852,#7fa4b2 60%,#c6d2d8);box-shadow:0 14px 20px rgba(0,0,0,.2)}

/* services */
.services{top:1183px;height:521px;background:var(--band)}
.services-shot{left:80px;top:115px;width:490px;height:406px;background:linear-gradient(160deg,#2f6fb5 0%,#6aa0d6 45%,#e8c89a 75%,#f2ede4 100%)}
.services .title{position:absolute;left:621px;top:130px;font-size:37px;line-height:1.2}
.services .copy{position:absolute;left:621px;top:218px;width:500px;font-size:14px}
.services .btn{left:621px;top:362px;width:198px;height:56px}
.arrow{position:absolute;top:277px;width:50px;height:50px;border-radius:50%;background:#3b3f43;display:flex;align-items:center;justify-content:center}
.tabs{top:1704px;height:106px;display:flex}
.tab{flex:1;display:flex;align-items:center;justify-content:center;text-align:center;color:var(--white);font-family:var(--head);font-weight:500;font-size:14.5px;line-height:1.2;background:var(--teal);border-right:1px solid rgba(255,255,255,.25);position:relative}
.tab.on{background:var(--green);font-weight:700}
.tab.alt{background:#15b9c9}
.tab.end{background:#33dd8c}

/* different */
.different{top:1810px;height:564px;background:linear-gradient(180deg,#fff 0%,#f6f8f9 100%)}
.different .eyebrow{position:absolute;left:80px;top:85px}
.different .title{position:absolute;left:80px;top:110px;font-size:42px}
.different .sub{position:absolute;left:80px;top:160px;font-size:16px}
.checklist{position:absolute;left:80px;top:216px;list-style:none}
.checklist li{display:flex;align-items:center;gap:24px;height:48px;font-size:15px;color:var(--ink)}
.diff-device{left:678px;top:172px;width:382px;height:310px;border-radius:10px;background:linear-gradient(160deg,#3a3f44,#b8c2c6 55%,#e8edee)}

/* portfolio */
.portfolio{top:2374px;height:752px;background:var(--band)}
.port-grid{left:80px;top:63px;width:520px;height:627px;background:linear-gradient(180deg,#4d9b5e 0%,#e9edf0 30%,#3a2f35 30%,#b23b32 55%,#f0f0f0 55%,#3a87c8 75%,#eef2f5 100%)}
.portfolio .eyebrow{position:absolute;left:672px;top:200px}
.portfolio .title{position:absolute;left:672px;top:224px;font-size:42px}
.portfolio .sub{position:absolute;left:672px;top:268px;font-size:16px}
.portfolio .copy{position:absolute;left:672px;top:298px;width:460px;font-size:14px}
.portfolio .btn{left:672px;top:405px;width:198px;height:52px}

/* team + news */
.team{top:3126px;height:445px;width:678px;background:linear-gradient(135deg,#1fbfb0 0%,#4fd0b4 50%,#2a9fa8 100%)}
.team-label{left:0;width:678px;top:278px;text-align:center;font-family:var(--head);font-weight:700;font-size:24px;color:var(--white);letter-spacing:.5px}
.news{top:3126px;left:678px;width:522px;height:445px;background:var(--band-2)}
.news .title{position:absolute;left:77px;top:44px;font-size:42px}
.card{position:absolute;left:77px;width:372px;height:114px;background:var(--white);padding:20px 22px;box-shadow:8px 8px 0 rgba(0,0,0,.06)}
.card .date{display:flex;align-items:center;gap:8px;font-size:13px;color:var(--teal)}
.card h3{margin-top:10px;font-family:var(--head);font-style:italic;font-weight:700;font-size:15px;color:var(--ink)}
.card p{margin-top:4px;font-style:italic;font-size:13px;color:var(--muted)}
.view-more{position:absolute;left:213px;top:392px;font-family:var(--head);font-style:italic;font-weight:700;font-size:16px;color:var(--teal);text-decoration:underline}

/* newsletter */
.newsletter{top:3571px;height:291px;background:var(--dark)}
.newsletter .title{position:absolute;left:77px;top:82px;font-size:42px;color:var(--white)}
.newsletter p{position:absolute;left:77px;top:138px;width:430px;font-style:italic;font-size:14px;line-height:1.45;color:#e8ecee}
.field{position:absolute;left:519px;top:106px;width:393px;height:56px;background:var(--white);display:flex;align-items:center;justify-content:space-between;padding:0 16px;font-size:15px;color:#444}
.newsletter .btn{left:926px;top:106px;width:194px;height:56px;font-size:21px}

/* footer */
.footer{top:3862px;height:414px;background:#fff}
.footer-brand{left:0;width:1200px;top:100px;display:flex;justify-content:center;align-items:center;gap:16px;font-family:var(--head);font-weight:800;font-size:34px;color:var(--ink);letter-spacing:1px}
.socials{left:0;width:1200px;top:236px;display:flex;justify-content:center;gap:24px}
.socials i{width:44px;height:44px;border:3px solid var(--ink);border-radius:8px}
.footer-links{left:0;width:1200px;top:306px;display:flex;justify-content:center;gap:14px;font-size:15px;color:var(--ink)}
.copyright{left:0;width:1200px;top:338px;text-align:center;font-size:15px;color:var(--ink)}
.copyright b{font-weight:700}
</style>
</head>
<body>

<section class="hero">
  <div class="hero-photo" role="img" aria-label="Photo of a person using a tablet showing a website"></div>
  <div class="nav">
    <div class="brand">BRIGHT &amp; STEADY</div>
    <nav class="menu">
      <span class="active"><svg width="16" height="14" viewBox="0 0 18 16"><path d="M1 8 L6 14 L17 1" stroke="#2fe08a" stroke-width="3" fill="none"/></svg>HOME</span>
      <span>SERVICES &amp; PRICING</span><span>OUR TEAM</span><span>CLIENT PORTFOLIO</span><span>CONTACT US</span>
    </nav>
    <div class="phone">555 010 7890</div>
  </div>
  <h1>The Design &amp; Marketing Team<br>That&nbsp; Always Puts Care &amp; Honesty<br>Before Profits</h1>
  <div class="btn">CONTACT US NOW</div>
  <svg class="hero-wedge" width="1200" height="140" viewBox="0 0 1200 140">
    <defs><linearGradient id="hw" x1="0" x2="1"><stop offset="0" stop-color="#19c3d6"/><stop offset="1" stop-color="#2fe08a"/></linearGradient></defs>
    <polygon points="400,140 1200,0 1200,140" fill="url(#hw)"/>
  </svg>
  <div class="dots"><i></i><i></i><i></i><i class="on"></i><i></i></div>
</section>

<section class="welcome">
  <svg class="abs" style="left:585px;top:-20px" width="600" height="540" viewBox="0 0 600 540">
    <circle cx="300" cy="268" r="250" fill="none" stroke="#e4e6e8" stroke-width="2"/>
    <circle cx="300" cy="268" r="205" fill="none" stroke="#d9dcde" stroke-width="2" stroke-dasharray="6 8"/>
    <circle cx="300" cy="268" r="160" fill="none" stroke="#e4e6e8" stroke-width="2"/>
  </svg>
  <div class="eyebrow abs">WELCOME TO</div>
  <div class="title">BRIGHT &amp; STEADY</div>
  <div class="sub">COMPANY SOLGAN</div>
  <p class="copy">We believe that honesty and integrity come before personal profits. We are a family owned and operated company. Our parents raised us to take care of each other and that's exactly what we've done. We treat each of our clients with the same loyalty and respect that we give each other</p>
  <div class="btn">LEARN MORE</div>
  <div class="abs welcome-device" role="img" aria-label="Laptop showing the company website"></div>
</section>

<section class="services">
  <div class="abs services-shot" role="img" aria-label="Illustration of a hand touching stacked website screens"></div>
  <h2 class="title">Website Design &amp;<br>Management</h2>
  <p class="copy">Lorem Ipsum is simply dummy text of the printing and typesetting industry. Lorem Ipsum has been the industry Lorem Ipsum is simply dummy text of the printing and typesetting industry. Lorem Ipsum has been the industry Lorem Ipsum is simply dummy text of the printing and typesetting industry. Lorem Ipsum has been the industry.</p>
  <div class="btn">LEARN MORE</div>
  <div class="arrow" style="left:9px"><svg width="14" height="20"><path d="M11 2 L3 10 L11 18" stroke="#fff" stroke-width="3" fill="none"/></svg></div>
  <div class="arrow" style="left:1141px"><svg width="14" height="20"><path d="M3 2 L11 10 L3 18" stroke="#fff" stroke-width="3" fill="none"/></svg></div>
</section>

<section class="tabs">
  <div class="tab on">Website<br>Design &amp;<br>Management</div>
  <div class="tab">Logo Design &amp;<br>Branding<br>Materials</div>
  <div class="tab">Online Store<br>Design &amp;<br>Management</div>
  <div class="tab">Local<br>SEO<br>Management</div>
  <div class="tab">Search<br>Engine<br>Optimization</div>
  <div class="tab">Social<br>Media<br>Marketing</div>
  <div class="tab">Marketing<br>Material &amp;<br>Print design</div>
  <div class="tab alt">Outsourcing<br>Management</div>
  <div class="tab end">Consulting</div>
</section>

<section class="different">
  <div class="eyebrow">WHAT</div>
  <h2 class="title">MAKES ME DIFFERENT ?</h2>
  <div class="sub">WHY CHOOSE BRIGHT &amp; STEADY</div>
  <ul class="checklist">
    <li><svg width="26" height="26" viewBox="0 0 26 26"><path d="M4 13 L10 19 L22 7" stroke="#18c6cf" stroke-width="3.5" fill="none" stroke-linecap="round" stroke-linejoin="round"/></svg>100% Risk Free Investment</li>
    <li><svg width="26" height="26" viewBox="0 0 26 26"><path d="M4 13 L10 19 L22 7" stroke="#18c6cf" stroke-width="3.5" fill="none" stroke-linecap="round" stroke-linejoin="round"/></svg>Customer Loyalty&nbsp; Program</li>
    <li><svg width="26" height="26" viewBox="0 0 26 26"><path d="M4 13 L10 19 L22 7" stroke="#18c6cf" stroke-width="3.5" fill="none" stroke-linecap="round" stroke-linejoin="round"/></svg>24/7 U.S. Based&nbsp; Customer Support</li>
    <li><svg width="26" height="26" viewBox="0 0 26 26"><path d="M4 13 L10 19 L22 7" stroke="#18c6cf" stroke-width="3.5" fill="none" stroke-linecap="round" stroke-linejoin="round"/></svg>Unmatched Personal Service</li>
    <li><svg width="26" height="26" viewBox="0 0 26 26"><path d="M4 13 L10 19 L22 7" stroke="#18c6cf" stroke-width="3.5" fill="none" stroke-linecap="round" stroke-linejoin="round"/></svg>Multiple Payment Options Available</li>
  </ul>
  <div class="abs diff-device" role="img" aria-label="Laptop showing a workspace photo on screen"></div>
</section>

<section class="portfolio">
  <svg class="abs" style="left:580px;top:0" width="620" height="700" viewBox="0 0 620 700">
    <path d="M5 0 V60 H108 V85" stroke="#18c6cf" stroke-width="2" stroke-dasharray="8 6" fill="none"/>
    <path d="M108 395 V490" stroke="#18c6cf" stroke-width="2" stroke-dasharray="8 6" fill="none"/>
    <path d="M115 490 V628 H620" stroke="#18c6cf" stroke-width="2" stroke-dasharray="8 6" fill="none"/>
    <rect x="100" y="145" width="14" height="14" transform="rotate(45 107 152)" fill="#18c6cf"/>
    <rect x="100" y="470" width="14" height="14" transform="rotate(45 107 477)" fill="#2fe08a"/>
  </svg>
  <div class="abs port-grid" role="img" aria-label="Collage of client website screenshots"></div>
  <div class="eyebrow">OUR</div>
  <h2 class="title">CLIENTS PORTFOLIO</h2>
  <div class="sub">OUR WORK</div>
  <p class="copy">Lorem Ipsum is simply dummy text of the printing and typesetting industry. Lorem Ipsum has been the industry Lorem Ipsum is simply dummy text of the printing and typesetting industry.</p>
  <div class="btn">VIEW ALL</div>
</section>

<section class="team" role="img" aria-label="Team photo with teal overlay">
  <svg class="abs" style="left:248px;top:230px" width="200" height="160" viewBox="0 0 200 160">
    <path d="M100 0 V160 M20 80 H180" stroke="#fff" stroke-width="2" opacity=".85"/>
  </svg>
  <div class="abs team-label">MEET OUR TEAM</div>
</section>

<section class="news">
  <h2 class="title">NEWS</h2>
  <article class="card" style="top:110px">
    <div class="date"><svg width="16" height="16"><rect x="1" y="3" width="14" height="12" fill="none" stroke="#18c6cf" stroke-width="2"/><path d="M1 6 H15" stroke="#18c6cf" stroke-width="2"/></svg>30 Oct 2017</div>
    <h3>BRIGHT &amp; STEADY NEWS</h3>
    <p>Lorem Ipsum is simply dummy text of the printing...</p>
  </article>
  <article class="card" style="top:252px">
    <div class="date"><svg width="16" height="16"><rect x="1" y="3" width="14" height="12" fill="none" stroke="#18c6cf" stroke-width="2"/><path d="M1 6 H15" stroke="#18c6cf" stroke-width="2"/></svg>30 Oct 2017</div>
    <h3>BRIGHT &amp; STEADY NEWS</h3>
    <p>Lorem Ipsum is simply dummy text of the printing...</p>
  </article>
  <div class="view-more">VIEW MORE</div>
</section>

<section class="newsletter">
  <h2 class="title">NEWSLETTER</h2>
  <p>Would you like to receive exclusive access to articles, white papers and our regular monthly newsletter?</p>
  <div class="field">Enter Email *<svg width="18" height="14"><rect x="1" y="1" width="16" height="12" fill="#18c6cf"/><path d="M1 1 L9 8 L17 1" stroke="#fff" stroke-width="1.5" fill="none"/></svg></div>
  <div class="btn">SUBSCRIBE</div>
  <svg class="abs" style="left:0;bottom:0" width="1200" height="70" viewBox="0 0 1200 70">
    <defs><linearGradient id="nw" x1="0" x2="1"><stop offset="0" stop-color="#19c3d6"/><stop offset="1" stop-color="#2fe08a"/></linearGradient></defs>
    <polygon points="340,70 1200,0 1200,70" fill="url(#nw)"/>
  </svg>
</section>

<footer class="footer">
  <div class="abs footer-brand"><i style="width:34px;height:34px;background:var(--teal);display:block"></i>BRIGHT &amp; STEADY</div>
  <div class="abs socials"><i></i><i></i><i></i></div>
  <nav class="abs footer-links"><span>Home</span>|<span>Services &amp; Pricing</span>|<span>Our Team</span>|<span>Clients/Portfolio</span>|<span>Contact Us</span></nav>
  <div class="abs copyright">© <b>BRIGHT &amp; STEADY COMPANY SOLGAN</b> 2017 All Right Reserved.</div>
</footer>

</body>
</html>
```